Builder of high-end, expensive tables and other furniture

Build a website that represents what we do. I want a luxury feel that appeals to those who can afford our products. We build very high end tables and other furniture using trees that have fallen or are standing dead. We never cut living trees. Trees are harvested, milled, and kiln dried. Then that lumber is meticulously turned into fine furniture using the best equipment. Our furniture prices range from $1,000-$20,000.

Trying to figure out how to raise my spend.

```html
<!DOCTYPE html>
<html lang="en">
<head>
<meta charset="UTF-8">
<title>Heartwood Atelier — Sustainable Luxury Furniture</title>
<link rel="stylesheet" href="https://fonts.googleapis.com/css2?family=Marcellus&family=Plus+Jakarta+Sans:wght@400;500;600&display=swap">
<style>
:root{
  --bg:#05070d;
  --panel:#12141a;
  --ink:#ffffff;
  --muted:#b9bcc4;
  --accent:#e8591f;
  --accent-2:#f39a4a;
  --label:#3f83d6;
  --line:#2a2d35;
  --display:"Marcellus", serif;
  --body:"Plus Jakarta Sans", sans-serif;
}
*{margin:0;padding:0;box-sizing:border-box}
html,body{width:1200px;height:3512px;overflow:hidden;background:var(--bg);color:var(--ink);font-family:var(--body)}
.page{position:relative;width:1200px;height:3512px}
.abs{position:absolute}
.brand{display:flex;align-items:center;gap:10px;font-family:var(--display);font-size:32px;color:var(--accent);white-space:nowrap}
.brand-dot{width:14px;height:14px;border-radius:50%;background:var(--accent)}
.label{font-size:15px;letter-spacing:2px;color:var(--label);font-weight:500}
.h2{font-family:var(--display);font-size:31px;line-height:38px;color:var(--ink)}
.btn-solid{display:flex;align-items:center;justify-content:center;border-radius:6px;background:linear-gradient(90deg,var(--accent),var(--accent-2));color:#fff;font-size:17px;font-weight:500}
.btn-ghost{display:flex;align-items:center;justify-content:center;border:1.5px solid #e6e6e6;border-radius:6px;color:#fff;font-size:18px;font-weight:500}

/* hero */
.hero{left:0;top:0;width:1200px;height:617px;background:radial-gradient(ellipse at 70% 40%,#36404f 0%,#1d232c 40%,#0b0d12 85%)}
.nav-links{left:663px;top:46px;display:flex;gap:34px;font-size:15px}
.nav-cta{left:925px;top:34px;width:153px;height:46px}
.hero-title{left:121px;top:203px;width:560px;font-family:var(--display);font-size:48px;line-height:54px}
.hero-sub{left:122px;top:382px;width:400px;font-size:15px;line-height:23px;color:#e4e4e4}
.hero-cta{left:122px;top:453px;width:154px;height:46px}

/* about */
.about-panel{left:121px;top:717px;width:956px;height:450px;background:var(--panel)}
.about-img{left:0;top:754px;width:550px;height:376px;background:linear-gradient(135deg,#6b4a2e,#2b2119 55%,#141414)}
.about-text{left:641px;top:907px;width:352px;font-size:14.5px;line-height:22.5px;color:var(--muted)}
.about-text strong{color:var(--accent);font-weight:500}
.about-btn{left:641px;top:1080px;width:155px;height:46px}

/* why us */
.why-img{left:642px;top:1343px;width:558px;height:582px;background:linear-gradient(160deg,#5a3a24,#2d1c12 50%,#6a4a32 90%)}
.features{left:119px;top:1495px;width:440px}
.feature{margin-bottom:26px}
.feature-head{display:flex;align-items:center;gap:12px;font-family:var(--display);font-size:14px;letter-spacing:.2px;text-transform:uppercase}
.feature-head svg{flex:none}
.feature p{margin-top:8px;font-size:13px;line-height:20px;color:var(--muted)}

/* gallery */
.center{left:0;width:1200px;text-align:center}
.slide{border-radius:18px}
.slide-left{left:-20px;top:2186px;width:291px;height:323px;background:linear-gradient(135deg,#3b2a1c,#1a1512)}
.slide-main{left:318px;top:2159px;width:564px;height:376px;background:linear-gradient(180deg,#2a2a2c,#1b1a1a 55%,#4a3a2e)}
.slide-right{left:929px;top:2186px;width:291px;height:323px;background:linear-gradient(135deg,#1c2433,#12151b)}
.soon{left:299px;top:2257px;width:602px;height:154px;background:rgba(10,10,12,.72);border-top:1px solid rgba(255,255,255,.35);border-bottom:1px solid rgba(255,255,255,.35);display:flex;align-items:center;justify-content:center;font-family:var(--body);font-size:38px;letter-spacing:11px;font-weight:500}
.arrow{width:38px;height:38px;border-radius:50%;display:flex;align-items:center;justify-content:center}
.dots{left:573px;top:2581px;display:flex;gap:9px;align-items:center}
.dots span{width:5px;height:5px;border-radius:50%;background:#5b5e66}
.dots span.on{width:13px;height:13px;border:1.5px solid #5b5e66;background:transparent}

/* contact band */
.cta-band{left:0;top:2708px;width:1200px;height:401px;background:radial-gradient(ellipse at 45% 25%,#5a3a22 0%,#2b1f17 40%,#14100e 85%)}
.cta-btn{left:522px;top:2975px;width:155px;height:46px}

/* footer */
.foot-title{font-family:var(--display);font-size:17px}
.foot-title::after{content:"";display:block;margin-top:12px;width:100px;height:1px;background:linear-gradient(90deg,transparent,#3b6cb5 60%,transparent)}
.foot-links{list-style:none;font-size:14.5px;line-height:29.5px;color:#d6d6d6}
.foot-contact{list-style:none;font-size:14.5px;color:#d6d6d6}
.foot-contact li{display:flex;gap:13px;margin-bottom:13px;line-height:23px}
.foot-contact svg{flex:none;margin-top:4px}
.socials{display:flex;gap:16px}
.socials span{width:18px;height:18px;border-radius:50%;border:1.6px solid var(--accent)}
.rule{left:121px;top:3405px;width:959px;height:1px;background:var(--line)}
</style>
</head>
<body>
<div class="page">

  <!-- Hero -->
  <section class="abs hero" role="img" aria-label="Photo of a dim dining nook with green velvet chairs around a wooden table"></section>
  <div class="abs brand" style="left:121px;top:32px"><span class="brand-dot"></span>Heartwood Atelier</div>
  <nav class="abs nav-links"><span>Home</span><span>About Us</span><span>Why Us</span></nav>
  <div class="abs btn-ghost nav-cta">Contact Us</div>
  <h1 class="abs hero-title">Discover Timeless Elegance in Sustainable Luxury Furniture</h1>
  <p class="abs hero-sub">Experience the Artistry of Nature Transformed into Unparalleled Furniture Creations</p>
  <div class="abs btn-solid hero-cta">Contact Us</div>

  <!-- About -->
  <div class="abs about-panel"></div>
  <div class="abs about-img" role="img" aria-label="Photo of a chevron-pattern walnut table on angular black steel legs"></div>
  <div class="abs label" style="left:637px;top:774px">ABOUT US</div>
  <h2 class="abs h2" style="left:641px;top:800px;width:420px">Redefining Luxury with Sustainable Craftsmanship</h2>
  <p class="abs about-text">At <strong>Heartwood Atelier LLC</strong>, we redefine the concept of luxury furniture with our unwavering commitment to sustainability and uncompromising craftsmanship. Our exquisite tables and furniture embody timeless elegance and offer a touch of opulence to the discerning clientele who appreciate the finer things in life.</p>
  <div class="abs btn-ghost about-btn">Read More</div>

  <!-- Why Us -->
  <div class="abs label" style="left:121px;top:1404px">WHY US</div>
  <h2 class="abs h2" style="left:121px;top:1424px">Sustainable Luxury Redefined</h2>
  <div class="abs features">
    <div class="feature">
      <div class="feature-head">
        <svg width="32" height="28" viewBox="0 0 32 28"><path d="M3 20h7l6 3 12-6" fill="none" stroke="#fff" stroke-width="2"/><circle cx="18" cy="9" r="6" fill="var(--accent)"/></svg>
        Sustainable Excellence</div>
      <p>We prioritize nature by using dead trees for furniture, promoting ecological harmony and sustainability while providing luxurious options.</p>
    </div>
    <div class="feature">
      <div class="feature-head">
        <svg width="32" height="28" viewBox="0 0 32 28"><circle cx="16" cy="12" r="9" fill="none" stroke="#fff" stroke-width="2"/><circle cx="16" cy="12" r="4" fill="var(--accent)"/></svg>
        Impeccable Craftsmanship</div>
      <p>Our experienced and passionate artisans use the finest techniques and tools to meticulously craft furniture with unparalleled quality.</p>
    </div>
    <div class="feature">
      <div class="feature-head">
        <svg width="32" height="28" viewBox="0 0 32 28"><rect x="4" y="4" width="22" height="20" fill="none" stroke="#fff" stroke-width="2"/><path d="M6 22L24 6M12 22L24 12" stroke="var(--accent)" stroke-width="2"/></svg>
        Exceptional Materials</div>
      <p>We choose superior lumber that's harvested, milled, and kiln-dried, enhancing its natural beauty to produce charming furniture.</p>
    </div>
    <div class="feature">
      <div class="feature-head">
        <svg width="32" height="28" viewBox="0 0 32 28"><rect x="5" y="6" width="22" height="12" rx="3" fill="var(--accent)"/><path d="M5 20h22M8 20v5M24 20v5" stroke="#fff" stroke-width="2"/></svg>
        Unparalleled Design</div>
      <p>Our furniture designs blend classic elegance and modern aesthetics, with styles ranging from minimalistic to ornate detailing to suit diverse tastes and interiors.</p>
    </div>
  </div>
  <div class="abs why-img" role="img" aria-label="Photo of a dark wooden side table beside a woven wicker basket"></div>

  <!-- Gallery -->
  <div class="abs label center" style="top:2018px">GALLERY</div>
  <h2 class="abs h2 center" style="top:2045px">Exquisite Collections</h2>
  <div class="abs slide slide-left" role="img" aria-label="Photo of a living room with a wooden coffee table"></div>
  <div class="abs slide slide-right" role="img" aria-label="Photo of a blue dresser with a table lamp"></div>
  <div class="abs slide slide-main" role="img" aria-label="Photo of a dining table with chairs against slatted wall panels"></div>
  <div class="abs soon">COMING SOON</div>
  <div class="abs arrow" style="left:299px;top:2322px;background:#1f2024">
    <svg width="10" height="10" viewBox="0 0 10 10"><path d="M6 2L3 5l3 3" fill="none" stroke="#888" stroke-width="1.4"/></svg></div>
  <div class="abs arrow" style="left:863px;top:2322px;background:var(--accent)">
    <svg width="10" height="10" viewBox="0 0 10 10"><path d="M4 2l3 3-3 3" fill="none" stroke="#fff" stroke-width="1.4"/></svg></div>
  <div class="abs dots"><span class="on"></span><span></span><span></span><span></span></div>

  <!-- Contact band -->
  <section class="abs cta-band" role="img" aria-label="Photo of a warm-lit workshop table with cups and tools"></section>
  <div class="abs label center" style="top:2845px">CONTACT US</div>
  <h2 class="abs center" style="top:2866px;font-family:var(--display);font-size:46px">Start Your Project Now!</h2>
  <p class="abs center" style="top:2932px;font-size:13px;color:#e2e2e2">to begin your custom project now, contact us directly</p>
  <div class="abs btn-solid cta-btn">Contact Us</div>

  <!-- Footer -->
  <div class="abs brand" style="left:124px;top:3162px"><span class="brand-dot"></span>Heartwood Atelier</div>
  <div class="abs" style="left:149px;top:3238px;font-size:17px">FOLLOW US</div>
  <div class="abs socials" style="left:149px;top:3272px"><span></span><span></span><span></span></div>

  <div class="abs" style="left:555px;top:3163px">
    <div class="foot-title">QUICK LINKS</div>
    <ul class="foot-links" style="margin-top:16px;margin-left:3px"><li>Home</li><li>About Us</li><li>Why us</li><li>Contact</li></ul>
  </div>
  <div class="abs" style="left:773px;top:3164px">
    <div class="foot-title">CONTACT</div>
    <ul class="foot-contact" style="margin-top:18px;width:250px">
      <li><svg width="13" height="16" viewBox="0 0 13 16"><path d="M6.5 15s5.5-5.5 5.5-9A5.5 5.5 0 0 0 1 6c0 3.5 5.5 9 5.5 9z" fill="var(--accent)"/><circle cx="6.5" cy="6" r="2" fill="var(--bg)"/></svg><span>418 Alder Grove Ln. Fernridge, Oregon 97402</span></li>
      <li><svg width="14" height="14" viewBox="0 0 14 14"><path d="M3 1l2.5 3-1.5 2a8 8 0 0 0 4 4l2-1.5 3 2.5-1.5 2C6 13 1 8 1 2.5z" fill="var(--accent)"/></svg><span>(541) 555-0187</span></li>
      <li><svg width="14" height="12" viewBox="0 0 14 12"><rect x="0.5" y="1" width="13" height="10" rx="1" fill="var(--accent)"/><path d="M1 2l6 5 6-5" fill="none" stroke="var(--bg)" stroke-width="1.2"/></svg><span>hello@heartwoodatelier.com</span></li>
    </ul>
  </div>
  <div class="abs rule"></div>
  <p class="abs center" style="top:3446px;font-size:13px;color:#bdbdbd">Copyright Heartwood Atelier | All rights reserved</p>

</div>
</body>
</html>
```